Website upgrade

I have two websites linked to the same business. One is for commercial and retail clients the other is for private and residential customers. I need a creative, modern thinking and bold designer to redesign my sites so that they look more professional and eye catching. The two sites are: www.marcusfieldingltd.com and www.pkrfittingservices.com

Target Market(s)

pkr fittings targets home owners and individuals who want work done to their property and marcus fielding targets commercial customers who want shopfitting work undertaken

Industry/Entity Type

Home Improvement

Number of Pages Required

5+ page

Font styles to use
Sans Serif

Colors
0255a3
3176b5
0292cd
85acd3
85cae6

Requirements
Must have
• i want a site to reflect my existing sites but with a bit more of a wow factor to draw customers in
Nice to have
• logo designed, video or slide show
Should not have
• blog page

```html
<!DOCTYPE html>
<html lang="en">
<head>
<meta charset="utf-8">
<title>Marcus Fielding Contracting Ltd</title>
<link href="https://fonts.googleapis.com/css2?family=Open+Sans:ital,wght@0,400;0,600;1,400&family=Roboto+Condensed:wght@400;700&family=Roboto:wght@300;400;500&display=swap" rel="stylesheet">
<style>
:root{
  --brand-dark:#0255a3;
  --brand:#3176b5;
  --brand-bright:#0292cd;
  --brand-soft:#85acd3;
  --brand-pale:#85cae6;
  --ink:#2b2f36;
  --ink-soft:#555b63;
  --muted:#7a8088;
  --line:#e1e4e8;
  --panel:#eef5fb;
  --footer:#f3f4f5;
  --white:#ffffff;
}
*{margin:0;padding:0;box-sizing:border-box}
html,body{width:1200px;height:2439px;overflow:hidden;background:var(--white)}
body{position:relative;font-family:"Open Sans",Arial,sans-serif;color:var(--ink-soft)}
a{color:inherit;text-decoration:none}

/* header */
.site-header{position:absolute;left:0;top:0;width:1200px;height:124px;background:var(--white)}
.brand{position:absolute;left:100px;top:38px;display:flex;align-items:center;gap:12px}
.brand-mark{width:26px;height:26px;background:var(--brand-bright)}
.brand-name{font-family:"Roboto Condensed",sans-serif;font-weight:400;font-size:27px;color:var(--ink-soft);line-height:1;letter-spacing:.2px}
.brand-tag{display:block;font-family:"Roboto Condensed",sans-serif;font-weight:400;font-size:14px;letter-spacing:3px;color:var(--ink-soft);margin-top:4px}
.contact-top{position:absolute;left:868px;top:40px;display:flex;gap:18px;align-items:center}
.contact-top .icon{width:36px;height:36px;border-radius:50%;background:var(--brand-bright);display:flex;align-items:center;justify-content:center}
.contact-top p{font-size:13px;line-height:22px;color:var(--ink-soft)}
.contact-top strong{font-weight:600;color:var(--ink)}

/* nav */
.main-nav{position:absolute;left:0;top:124px;width:1200px;height:52px;background:linear-gradient(#10a6e3,#0292cd)}
.main-nav a{position:absolute;top:0;height:52px;line-height:52px;font-family:"Roboto",sans-serif;font-size:13px;color:var(--white);text-transform:uppercase}
.main-nav a.active{left:99px;width:104px;text-align:center;background:#2a2d31}

/* hero */
.hero{position:absolute;left:0;top:176px;width:1200px;height:515px;background:linear-gradient(100deg,#3c4c62 0%,#8d6f52 22%,#c9ad8d 45%,#e6d8c6 70%,#cdb69a 100%)}
.hero-box{position:absolute;left:642px;top:174px;width:459px;height:187px;background:rgba(255,255,255,.82);padding:20px 0 0 18px}
.hero-box h1{font-family:"Roboto Condensed",sans-serif;font-weight:700;font-size:37px;line-height:44px;color:#2e3238;text-transform:uppercase}
.hero-box p{margin-top:10px;font-size:14px;line-height:24px;color:#4a4f56}
.hero-arrow{position:absolute;top:254px;width:34px;height:34px;border-radius:50%;background:rgba(40,40,40,.75);display:flex;align-items:center;justify-content:center}

/* welcome */
.welcome-title{position:absolute;left:0;top:733px;width:1200px;text-align:center;font-family:"Roboto",sans-serif;font-weight:400;font-size:29px;color:#2b2f36;text-transform:uppercase}
.welcome-title span{color:var(--brand-bright)}
.welcome-text{position:absolute;left:145px;top:786px;width:910px;text-align:center;font-size:11px;line-height:20px;color:var(--ink-soft)}
.service-card{position:absolute;top:880px;width:315px}
.service-card .photo{height:185px;border-bottom:3px solid var(--brand-bright)}
.service-card h3{margin-top:20px;font-family:"Roboto",sans-serif;font-weight:300;font-size:19px;color:var(--ink)}
.service-card h4{margin-top:4px;font-weight:400;font-size:13px;color:var(--ink)}
.service-card p{margin-top:8px;font-size:11.5px;line-height:22px}
.read-more{display:inline-flex;align-items:center;gap:8px;margin-top:10px;font-size:12px;color:var(--brand);text-transform:uppercase}

/* fittings */
.fittings{position:absolute;left:0;top:1293px;width:1200px;height:463px;background:linear-gradient(90deg,#f2f7fc,#e4eff9 60%,#eaf3fb);border-top:1px solid var(--line)}
.fittings h2{position:absolute;left:99px;top:68px;font-family:"Roboto",sans-serif;font-weight:400;font-size:29px;color:#2b3a55;text-transform:uppercase}
.fittings .intro{position:absolute;left:99px;top:115px;width:545px;font-size:11.5px;line-height:23px}
.ticks{position:absolute;left:99px;top:256px;list-style:none}
.ticks li{display:flex;align-items:center;gap:12px;height:28.3px;font-size:13px}
.video{position:absolute;left:681px;top:66px;width:420px;height:317px;background:linear-gradient(135deg,#5c3f2a,#a78462 45%,#d9cfb8 75%,#8c6a49);border:5px solid var(--white);box-shadow:0 1px 4px rgba(0,0,0,.2)}
.play{position:absolute;left:180px;top:132px;width:52px;height:38px;border-radius:8px;background:rgba(255,255,255,.75);display:flex;align-items:center;justify-content:center}

/* reviews */
.reviews-title{position:absolute;left:0;top:1814px;width:1200px;text-align:center;font-family:"Roboto",sans-serif;font-weight:400;font-size:26px;color:#4a4f56;text-transform:uppercase}
.review{position:absolute;top:1886px;width:480px;height:166px;border-left:1px solid var(--line);padding-left:24px}
.review blockquote{font-style:italic;font-size:14px;line-height:24px;color:var(--ink-soft);width:420px}
.review blockquote::before{content:"\201C";font-size:22px;color:#888;margin-right:2px}
.avatar{position:absolute;left:25px;top:96px;width:74px;height:74px;border-radius:50%;background:linear-gradient(#c9b6a2,#8b7766);border:2px solid #ddd}
.reviewer{position:absolute;left:125px;top:114px;font-style:italic;font-size:13px;line-height:21px;color:var(--brand)}
.reviewer b{font-weight:400;text-transform:uppercase}

/* footer */
.site-footer{position:absolute;left:0;top:2130px;width:1200px;height:252px;background:var(--footer)}
.footer-col{position:absolute;top:32px}
.footer-col h5{font-family:"Roboto",sans-serif;font-weight:400;font-size:17px;color:#2b2f36;text-transform:uppercase;margin-bottom:14px}
.footer-col h5 span{color:var(--brand-bright)}
.footer-col ul{list-style:none}
.footer-col li{font-size:11.5px;line-height:25.8px;color:var(--ink)}
.newsletter p{font-size:11px;line-height:19px;width:265px;margin-bottom:12px}
.field{width:262px;height:40px;background:var(--white);border:1px solid var(--line);font-size:11px;line-height:38px;padding-left:12px;color:var(--ink);margin-bottom:10px}
.subscribe{position:absolute;left:163px;top:0;width:99px;height:40px;background:var(--brand-dark);color:var(--white);font-size:12px;text-align:center;line-height:40px;text-transform:uppercase}
.footer-brand .brand-name{font-size:22px}
.footer-brand .brand-tag{font-size:12px}
.footer-address{font-size:12px;line-height:22px;color:var(--ink-soft);margin-top:16px}
.footer-contact{display:flex;align-items:center;gap:14px;font-size:12px;color:var(--ink);margin-top:10px}
.bottom-bar{position:absolute;left:0;top:2382px;width:1200px;height:57px;background:var(--brand-dark);color:var(--white)}
.bottom-bar p{position:absolute;left:99px;top:0;line-height:57px;font-size:11px}
.socials{position:absolute;left:1000px;top:17px;display:flex;gap:6px}
.socials span{width:22px;height:22px;border-radius:50%;border:1px solid rgba(255,255,255,.8)}
</style>
</head>
<body>

<header class="site-header">
  <div class="brand">
    <div class="brand-mark"></div>
    <div><span class="brand-name">MARCUS FIELDING</span><span class="brand-tag">Contracting Ltd</span></div>
  </div>
  <div class="contact-top">
    <div class="icon"><svg width="16" height="16" viewBox="0 0 24 24"><path fill="#fff" d="M6.6 10.8a15 15 0 0 0 6.6 6.6l2.2-2.2a1 1 0 0 1 1-.25 11.4 11.4 0 0 0 3.6.6 1 1 0 0 1 1 1V20a1 1 0 0 1-1 1A17 17 0 0 1 3 4a1 1 0 0 1 1-1h3.5a1 1 0 0 1 1 1c0 1.25.2 2.45.6 3.6a1 1 0 0 1-.25 1z"/></svg></div>
    <p>Ph:&nbsp; 07700 914582<br><strong>info@marcusfieldingltd.com</strong></p>
  </div>
</header>

<nav class="main-nav">
  <a class="active" href="#">Home</a>
  <a style="left:238px" href="#">About us</a>
  <a style="left:353px" href="#">Services</a>
  <a style="left:468px" href="#">Job vacancies</a>
  <a style="left:616px" href="#">Testimonials</a>
  <a style="left:759px" href="#">Clients</a>
  <a style="left:863px" href="#">Quotes &amp; Estimates</a>
  <a style="left:1047px" href="#">Contact</a>
</nav>

<section class="hero" role="img" aria-label="Tradesman with hard hat, hammer and tool belt in a timber-framed interior under construction">
  <div class="hero-arrow" style="left:46px"><svg width="12" height="12" viewBox="0 0 12 12"><path d="M8 1L3 6l5 5" stroke="#fff" stroke-width="2" fill="none"/></svg></div>
  <div class="hero-box">
    <h1>Marcus Fielding<br>Property Maintenance</h1>
    <p>Marcus Fielding Contracting provide Project Management &amp;<br>Interior fit-out services to all types of commercial</p>
  </div>
  <div class="hero-arrow" style="left:1126px"><svg width="12" height="12" viewBox="0 0 12 12"><path d="M4 1l5 5-5 5" stroke="#fff" stroke-width="2" fill="none"/></svg></div>
</section>

<h2 class="welcome-title">Welcome to <span>Marcus Fielding Contracting</span></h2>
<p class="welcome-text">Lorem ipsum dolor sit amet, consectetur adipiscing elit, sed do eiusmod tempor incididunt ut labore et dolore magna aliqua. Ut enim ad minim veniam, quis nostrud exercitation ullamco laboris nisi ut aliquip ex ea commodo consequat. Duis aute irure dolor in reprehenderit in voluptate velit esse cillum dolore eu fugiat nulla pariatur. Excepteur sint occaecat cupidatat non proident, sunt in culpa qui officia deserunt mollit anim id est laborum</p>

<article class="service-card" style="left:100px">
  <div class="photo" role="img" aria-label="Luxury kitchen with dark wood cabinets" style="background:linear-gradient(135deg,#3a2418,#7a5236 50%,#c8b49a)"></div>
  <h3>Property Services</h3><h4>Refurbishment, Maintenance &amp; Repairs</h4>
  <p>Lorem ipsum dolor sit amet, consectetur adipiscing elit, sed do eiusmod tempor incididunt ut labore et dolore magna aliqua. Ut enim ad minim veniam, quis nostrud</p>
  <a class="read-more" href="#">Read more <svg width="14" height="10" viewBox="0 0 14 10"><path d="M0 5h12M8 1l4 4-4 4" stroke="#3176b5" stroke-width="1.4" fill="none"/></svg></a>
</article>
<article class="service-card" style="left:444px">
  <div class="photo" role="img" aria-label="Hard hat on plans with cranes at sunset" style="background:linear-gradient(160deg,#f7b733,#e07b14 45%,#8a4a12)"></div>
  <h3>Site Services</h3><h4>Project &amp; Site Management</h4>
  <p>Lorem ipsum dolor sit amet, consectetur adipiscing elit, sed do eiusmod tempor incididunt ut labore et dolore magna aliqua. Ut enim ad minim veniam, quis nostrud</p>
  <a class="read-more" href="#">Read more <svg width="14" height="10" viewBox="0 0 14 10"><path d="M0 5h12M8 1l4 4-4 4" stroke="#3176b5" stroke-width="1.4" fill="none"/></svg></a>
</article>
<article class="service-card" style="left:787px">
  <div class="photo" role="img" aria-label="Open-plan living room with stone wall and spiral staircase" style="background:linear-gradient(135deg,#4a3326,#a9754a 55%,#e9d6b8)"></div>
  <h3>Contracting (sub-contracting)</h3><h4>Refurbishment, Maintenance &amp; Repairs</h4>
  <p>Lorem ipsum dolor sit amet, consectetur adipiscing elit, sed do eiusmod tempor incididunt ut labore et dolore magna aliqua. Ut enim ad minim veniam, quis nostrud</p>
  <a class="read-more" href="#">Read more <svg width="14" height="10" viewBox="0 0 14 10"><path d="M0 5h12M8 1l4 4-4 4" stroke="#3176b5" stroke-width="1.4" fill="none"/></svg></a>
</article>

<section class="fittings">
  <h2>PKR Fittings Services</h2>
  <p class="intro">For more than two decades, PKR Fittings Services have delivered careful, good-value joinery, carpentry &amp; home services across the Calderbrook district. Our core trades are Joinery &amp; Carpentry, and we also fit kitchens, install bathrooms, carry out small building works and refresh tired properties. We take on routine upkeep and a wide variety of jobs in and around the home. Whether you are a home owner after a quick repair or a landlord needing ongoing care for your property, PKR Fittings Services are ready to help.</p>
  <ul class="ticks">
    <li><svg width="12" height="10" viewBox="0 0 12 10"><path d="M1 5l3.5 3.5L11 1" stroke="#0292cd" stroke-width="2.2" fill="none"/></svg>Joinery manufacture &amp; Installation</li>
    <li><svg width="12" height="10" viewBox="0 0 12 10"><path d="M1 5l3.5 3.5L11 1" stroke="#0292cd" stroke-width="2.2" fill="none"/></svg>General property repairs &amp; maintenance</li>
    <li><svg width="12" height="10" viewBox="0 0 12 10"><path d="M1 5l3.5 3.5L11 1" stroke="#0292cd" stroke-width="2.2" fill="none"/></svg>Wood work repairs &amp; restoration</li>
    <li><svg width="12" height="10" viewBox="0 0 12 10"><path d="M1 5l3.5 3.5L11 1" stroke="#0292cd" stroke-width="2.2" fill="none"/></svg>From knock throughs to loft conversions</li>
    <li><svg width="12" height="10" viewBox="0 0 12 10"><path d="M1 5l3.5 3.5L11 1" stroke="#0292cd" stroke-width="2.2" fill="none"/></svg>Internal &amp; External door services</li>
  </ul>
  <div class="video" role="img" aria-label="Video still of a fitted kitchen with wooden worktops">
    <div class="play"><svg width="16" height="18" viewBox="0 0 16 18"><path d="M2 1l13 8-13 8z" fill="#555"/></svg></div>
  </div>
</section>

<h2 class="reviews-title">Customer Reviews</h2>
<div class="review" style="left:130px">
  <blockquote>Lorem ipsum dolor sit amet, consectetur adipisicing elit, sed do eiusmod tempor incididunt ut labore et dolore magna aliqua Unde omnis, consequuntur.</blockquote>
  <div class="avatar" role="img" aria-label="Customer portrait"></div>
  <p class="reviewer"><b>Helena Brooks</b><br>Marcus Fielding,</p>
</div>
<div class="review" style="left:650px">
  <blockquote>Lorem ipsum dolor sit amet, consectetur adipisicing elit, sed do eiusmod tempor incididunt ut labore et dolore magna aliqua Unde omnis, consequuntur.</blockquote>
  <div class="avatar" role="img" aria-label="Customer portrait"></div>
  <p class="reviewer"><b>Daniel Ashworth</b><br>Marcus Fielding ,</p>
</div>

<footer class="site-footer">
  <div class="footer-col" style="left:99px">
    <h5>PKR Fittings</h5>
    <ul><li>Project Management</li><li>Project Planning</li><li>Roll-Out program management</li><li>Design Management</li><li>Procurement/outsourcing</li><li>Site Management</li></ul>
  </div>
  <div class="footer-col" style="left:338px">
    <h5>Company</h5>
    <ul><li>Services</li><li>Clients</li><li>Testimonials</li><li>Quotes &amp; Estimates</li><li>Contact</li><li>Job Vacancies</li></ul>
  </div>
  <div class="footer-col newsletter" style="left:532px">
    <h5>Sign up for <span>Newsletter</span></h5>
    <p>Excepteur sint occaecat cupidatat non proident, sunt in culpa qui officia deserunt</p>
    <div class="field">Enter Name</div>
    <div style="position:relative"><div class="field">Enter Email</div><div class="subscribe">Subscribe</div></div>
  </div>
  <div class="footer-col footer-brand" style="left:873px;top:36px">
    <div style="display:flex;align-items:center;gap:10px">
      <div class="brand-mark" style="width:22px;height:22px"></div>
      <div><span class="brand-name">MARCUS FIELDING</span><span class="brand-tag">Contracting Ltd</span></div>
    </div>
    <p class="footer-address">Marcus Fielding Contracting<br>48 Elmstead Road, Leeds</p>
    <div class="footer-contact"><svg width="16" height="16" viewBox="0 0 24 24"><path fill="none" stroke="#3176b5" stroke-width="1.6" d="M6.6 10.8a15 15 0 0 0 6.6 6.6l2.2-2.2a1 1 0 0 1 1-.25 11.4 11.4 0 0 0 3.6.6 1 1 0 0 1 1 1V20a1 1 0 0 1-1 1A17 17 0 0 1 3 4a1 1 0 0 1 1-1h3.5a1 1 0 0 1 1 1c0 1.25.2 2.45.6 3.6a1 1 0 0 1-.25 1z"/></svg>+1&nbsp; 07700 914582</div>
    <div class="footer-contact"><svg width="16" height="12" viewBox="0 0 16 12"><rect x=".8" y=".8" width="14.4" height="10.4" fill="none" stroke="#3176b5" stroke-width="1.4"/><path d="M1 1l7 6 7-6" fill="none" stroke="#3176b5" stroke-width="1.4"/></svg>sales@marcusfieldingltd.com</div>
  </div>
</footer>

<div class="bottom-bar">
  <p>©2015 - 2016&nbsp; MARCUS FIELDING CONTRACTING LTD .. All Rights Reserved.</p>
  <div class="socials"><span></span><span></span><span></span><span></span></div>
</div>

</body>
</html>
```